Residential & commercial landscaping company

Updated business cards for commercial and landscaping company. We would like to keep out logo, but just need a more updated business card.

```html
<!DOCTYPE html>
<html lang="en">
<head>
<meta charset="utf-8">
<title>Greenridge Grounds – Business Card</title>
<link href="https://fonts.googleapis.com/css2?family=Lobster+Two:wght@700&family=Questrial&display=swap" rel="stylesheet">
<style>
  :root {
    --stage: #1c1c1c;
    --card: #ffffff;
    --ink: #1a1a1a;
    --leaf: #4e8a2a;
    --lime: #8cc63f;
    --grass-light: #9ed64a;
    --grass-dark: #3f8f1f;
    --forest: #2f6b2a;
    --teal: #00806a;
    --sea: #009a78;
    --sage: #3c7f5c;
    --pale: #a9d86e;
  }
  * { box-sizing: border-box; margin: 0; padding: 0; }
  html, body { width: 1200px; height: 1200px; overflow: hidden; }
  body {
    background: var(--stage);
    font-family: "Questrial", "Century Gothic", sans-serif;
    position: relative;
  }
  .sheet-title {
    position: absolute; left: 180px; top: 30px;
    font-family: "Lobster Two", cursive;
    font-size: 46px; color: #fff;
  }
  .card {
    position: absolute; left: 180px;
    width: 840px; height: 480px;
    background: var(--card);
    border-radius: 26px;
    overflow: hidden;
  }
  .card--front { top: 110px; }
  .card--back { top: 630px; }

  .brand {
    display: flex; align-items: center; gap: 14px;
    font-size: 50px; color: var(--ink); letter-spacing: 0.5px;
    white-space: nowrap;
  }
  .brand__dot {
    width: 34px; height: 34px; border-radius: 50%;
    background: var(--lime); flex: none;
  }
  .card--front .brand {
    position: absolute; top: 150px; left: 0; right: 0; justify-content: center;
  }
  .grass {
    position: absolute; left: 0; right: 0; bottom: 0; height: 200px;
    background: linear-gradient(to bottom, rgba(158,214,74,0) 0%, var(--grass-light) 35%, var(--grass-dark) 100%);
  }

  .card--back .brand {
    position: absolute; top: 150px; left: 44px; font-size: 38px; gap: 12px;
  }
  .card--back .brand__dot { width: 28px; height: 28px; }
  .contact {
    position: absolute; right: 36px; top: 64px;
    text-align: right;
  }
  .contact__name { font-size: 30px; font-weight: 700; color: var(--ink); letter-spacing: 0.5px; }
  .contact__role { font-size: 17px; font-weight: 700; color: var(--leaf); margin-top: 4px; margin-right: 40px; }
  .contact__list { list-style: none; margin-top: 26px; }
  .contact__item {
    display: flex; align-items: center; justify-content: flex-end; gap: 14px;
    font-size: 19px; color: var(--ink); height: 38px;
  }
  .contact__text { white-space: nowrap; }
  .contact__text em { font-style: normal; color: var(--leaf); }
  .icon {
    width: 26px; height: 26px; border-radius: 50%; flex: none;
    background: var(--lime); display: flex; align-items: center; justify-content: center;
  }
  .icon svg { width: 14px; height: 14px; }
  .waves { position: absolute; left: 0; bottom: 0; width: 840px; height: 200px; }
</style>
</head>
<body>
  <h1 class="sheet-title">Business Card- 2</h1>

  <section class="card card--front">
    <div class="brand"><span class="brand__dot"></span>Greenridge Grounds</div>
    <div class="grass" role="img" aria-label="Illustration of a strip of green lawn grass along the bottom edge"></div>
  </section>

  <section class="card card--back">
    <div class="brand"><span class="brand__dot"></span>Greenridge Grounds</div>

    <div class="contact">
      <p class="contact__name">Daniel Hartwell</p>
      <p class="contact__role">Project Manager</p>
      <ul class="contact__list">
        <li class="contact__item"><span class="contact__text">555-214-0380 ext. 412</span>
          <span class="icon"><svg viewBox="0 0 24 24"><path fill="#fff" d="M6.6 10.8a15.1 15.1 0 0 0 6.6 6.6l2.2-2.2c.3-.3.7-.4 1-.2 1.1.4 2.3.6 3.6.6.6 0 1 .4 1 1V20c0 .6-.4 1-1 1A17 17 0 0 1 3 4c0-.6.4-1 1-1h3.5c.6 0 1 .4 1 1 0 1.3.2 2.5.6 3.6.1.3 0 .7-.2 1z"/></svg></span>
        </li>
        <li class="contact__item"><span class="contact__text">555-687-2945</span>
          <span class="icon"><svg viewBox="0 0 24 24"><rect x="6" y="2" width="12" height="20" rx="2" fill="#fff"/><rect x="8" y="5" width="8" height="11" fill="#8cc63f"/></svg></span>
        </li>
        <li class="contact__item"><span class="contact__text">dan@<em>GreenridgeGrounds</em>.com</span>
          <span class="icon"><svg viewBox="0 0 24 24"><rect x="3" y="5" width="18" height="14" rx="1.5" fill="#fff"/><path d="M3.5 6l8.5 7 8.5-7" fill="none" stroke="#8cc63f" stroke-width="1.8"/></svg></span>
        </li>
        <li class="contact__item"><span class="contact__text">www.<em>GreenridgeGrounds</em>.com</span>
          <span class="icon"><svg viewBox="0 0 24 24"><circle cx="12" cy="12" r="9" fill="none" stroke="#fff" stroke-width="2"/><ellipse cx="12" cy="12" rx="4" ry="9" fill="none" stroke="#fff" stroke-width="1.6"/><path d="M3 12h18" stroke="#fff" stroke-width="1.6"/></svg></span>
        </li>
      </ul>
    </div>

    <svg class="waves" viewBox="0 0 840 200" preserveAspectRatio="none" aria-hidden="true">
      <path d="M0 20 C180 -10 330 40 480 110 C620 170 740 150 840 140 L840 200 L0 200 Z" fill="var(--lime)"/>
      <path d="M0 40 C180 10 340 60 480 125 C620 180 740 165 840 155 L840 200 L0 200 Z" fill="var(--sage)"/>
      <path d="M0 60 C170 30 340 80 490 140 C630 190 750 175 840 170 L840 200 L0 200 Z" fill="var(--sea)"/>
      <path d="M0 78 C160 55 320 100 470 150 C610 195 740 190 840 185 L840 200 L0 200 Z" fill="var(--teal)"/>
      <path d="M0 100 C150 80 300 120 440 165 C560 200 700 200 840 196 L840 200 L0 200 Z" fill="var(--forest)"/>
      <path d="M0 125 C140 110 280 150 400 185 L420 200 L0 200 Z" fill="var(--lime)"/>
      <path d="M0 52 C170 24 330 72 480 134 C620 188 740 172 840 164" fill="none" stroke="var(--pale)" stroke-width="4"/>
      <path d="M0 90 C160 68 320 110 460 158 C600 200 720 194 840 190" fill="none" stroke="var(--pale)" stroke-width="3"/>
    </svg>
  </section>
</body>
</html>
```